ultra-minimalist business card

front (black background, matte):

tarik b. hosseny
writer | photographer
get@tarikhosseny.com

back (white background, matte):

a picture speaks a thousand words;
a word draws a thousand pictures.

www.tarikhosseny.com

all text should be small (white or silver - as long as it shows against the black - on the front; black or gray - as long as it shows against the white - on the back).

feel free to get creative in terms of arrangement, alignment, and font type, but remember, the overall style is minimalist, so nothing too fancy, please.

thanks.

```html
<!DOCTYPE html>
<html lang="en">
<head>
<meta charset="utf-8">
<title>tarik b. hosseny — business card</title>
<link rel="stylesheet" href="https://fonts.googleapis.com/css2?family=Quicksand:wght@300;400&display=swap">
<style>
  :root {
    --backdrop: #9b9b9b;
    --card-front: #1d1e20;
    --card-back: #f2f2f2;
    --ink-light: #f1f1f1;
    --ink-silver: #cfcfcf;
    --ink-dark: #2a2a2a;
  }
  html, body {
    margin: 0;
    padding: 0;
    width: 1200px;
    height: 1200px;
    overflow: hidden;
    background: var(--backdrop);
  }
  .canvas {
    width: 1200px;
    height: 1200px;
    display: flex;
    flex-direction: column;
    align-items: center;
    justify-content: center;
    gap: 60px;
  }
  .card {
    position: relative;
    width: 900px;
    height: 514px;
    box-sizing: border-box;
    box-shadow: 0 10px 30px rgba(0, 0, 0, 0.25);
  }
  .card--front {
    background: var(--card-front);
  }
  .card--back {
    background: var(--card-back);
  }
  .card__name {
    position: absolute;
    left: 96px;
    top: 78px;
    margin: 0;
    font-family: "Quicksand", sans-serif;
    font-weight: 400;
    font-size: 34px;
    letter-spacing: 3px;
    color: var(--ink-light);
    text-transform: uppercase;
  }
  .card__details {
    position: absolute;
    right: 96px;
    top: 168px;
    text-align: right;
    font-family: "Quicksand", sans-serif;
    font-weight: 300;
    color: var(--ink-silver);
  }
  .card__role {
    margin: 0 0 62px;
    font-size: 24px;
    letter-spacing: 0.5px;
  }
  .card__contact {
    margin: 0;
    font-size: 25px;
    line-height: 1.35;
    color: var(--ink-light);
    font-weight: 400;
  }
  .card__quote {
    position: absolute;
    left: 96px;
    top: 110px;
    margin: 0;
    font-family: "Quicksand", sans-serif;
    font-weight: 300;
    font-size: 25px;
    line-height: 1.6;
    color: var(--ink-dark);
  }
</style>
</head>
<body>
  <main class="canvas">
    <section class="card card--front" aria-label="Card front">
      <h1 class="card__name">tarik b. hosseny</h1>
      <div class="card__details">
        <p class="card__role">writer | photographer</p>
        <p class="card__contact">get@tarikhosseny.com<br>www.tarikhosseny.com</p>
      </div>
    </section>
    <section class="card card--back" aria-label="Card back">
      <p class="card__quote">a picture speaks a thousand words;<br>a word draws a thousand pictures.</p>
    </section>
  </main>
</body>
</html>
```